I am looking for a modern, clean and neat design for a reflexology and well being business. The business name is Lumen Orto (this is an old Latin word for wellbeing). The colours I would like are purple, white and grey. I am open to suggestions for pictures such as healing or working hands, a pair of feet, images that represent my business that you may think of....... or maybe you think no images at all would be best? My tag line is: "Relax, Renew, Revive" or "Find you balance......... Relax, Renew, Revive" I can decide which I want so I would like to see what both would look like. I would like space on the back to write the client's appointment date and time (more than once)

```html
<!DOCTYPE html>
<html lang="en">
<head>
<meta charset="utf-8">
<title>Lumen Orto – Business Card</title>
<link rel="stylesheet" href="https://fonts.googleapis.com/css2?family=Open+Sans:wght@400;600;700&display=swap">
<style>
  :root {
    --purple: #9a00b4;
    --purple-text: #8c1aa8;
    --white: #ffffff;
    --grey-text: #555555;
    --dots: #666666;
    --divider: #e4d2ea;
    --backdrop: #3a3b3f;
  }
  * { margin: 0; padding: 0; box-sizing: border-box; }
  html, body { width: 1200px; height: 864px; overflow: hidden; }
  body {
    background: var(--backdrop);
    font-family: "Open Sans", Arial, sans-serif;
    display: flex;
    flex-direction: column;
    align-items: center;
    justify-content: center;
    gap: 40px;
  }
  .card {
    width: 580px;
    height: 332px;
    border-radius: 4px;
    position: relative;
  }

  /* Appointment side */
  .appointment-card {
    background: var(--white);
    color: var(--purple-text);
    padding: 26px 40px 0;
  }
  .appointment-title {
    text-align: center;
    font-size: 19px;
    font-weight: 700;
    margin-bottom: 16px;
  }
  .field-row {
    display: flex;
    align-items: flex-end;
    font-size: 13px;
    font-weight: 600;
    margin-bottom: 14px;
  }
  .field-label { white-space: nowrap; margin-right: 6px; }
  .field-line {
    border-bottom: 2px dotted var(--dots);
    height: 12px;
  }
  .field-line.long { flex: 1; }
  .field-line.short { width: 130px; margin-right: 16px; }
  .field-suffix { margin-left: 6px; white-space: nowrap; font-weight: 400; }
  .appointment-slot {
    border-top: 1px solid var(--divider);
    padding-top: 12px;
    margin-bottom: 12px;
  }
  .slot-number {
    font-weight: 700;
    margin-right: 10px;
    white-space: nowrap;
  }
  .day-row {
    display: flex;
    justify-content: space-between;
  }
  .day {
    display: flex;
    align-items: center;
    gap: 5px;
    font-size: 13px;
    color: var(--grey-text);
  }
  .day-box {
    width: 17px;
    height: 14px;
    border: 1.5px solid var(--purple-text);
  }
  .notice {
    text-align: center;
    font-size: 13.5px;
    font-weight: 700;
    padding-top: 4px;
  }

  /* Contact side */
  .contact-card {
    background: var(--purple);
    color: var(--white);
    padding: 34px 36px;
  }
  .brand {
    display: flex;
    align-items: center;
    gap: 22px;
    margin-bottom: 22px;
  }
  .brand-dot {
    width: 58px;
    height: 58px;
    border-radius: 50%;
    background: var(--white);
  }
  .brand-name {
    font-size: 44px;
    font-weight: 400;
    letter-spacing: 1px;
  }
  .person-name { font-size: 18px; font-weight: 700; line-height: 1.1; }
  .person-role { font-size: 13px; margin-bottom: 14px; }
  .address { font-size: 14px; line-height: 1.2; margin-bottom: 10px; }
  .contact-list { list-style: none; font-size: 14px; line-height: 1.45; }
  .contact-list li { display: flex; align-items: center; gap: 10px; }
  .contact-icon { width: 11px; height: 11px; fill: var(--white); flex: none; }
  .tagline {
    position: absolute;
    right: 36px;
    bottom: 34px;
    font-size: 16px;
    font-weight: 600;
    letter-spacing: 0.5px;
  }
</style>
</head>
<body>

  <section class="card appointment-card">
    <h2 class="appointment-title">Your Next Appointment on</h2>
    <div class="field-row">
      <span class="field-label">Name :</span>
      <span class="field-line long"></span>
    </div>

    <div class="appointment-slot">
      <div class="field-row">
        <span class="slot-number">1.</span>
        <span class="field-label">Date :</span>
        <span class="field-line short"></span>
        <span class="field-label">Time :</span>
        <span class="field-line short"></span>
        <span class="field-suffix">AM / PM</span>
      </div>
      <div class="day-row">
        <span class="day"><span class="day-box"></span>MON</span>
        <span class="day"><span class="day-box"></span>TUE</span>
        <span class="day"><span class="day-box"></span>WED</span>
        <span class="day"><span class="day-box"></span>THU</span>
        <span class="day"><span class="day-box"></span>FRI</span>
        <span class="day"><span class="day-box"></span>SAT</span>
      </div>
    </div>

    <div class="appointment-slot">
      <div class="field-row">
        <span class="slot-number">2.</span>
        <span class="field-label">Date :</span>
        <span class="field-line short"></span>
        <span class="field-label">Time :</span>
        <span class="field-line short"></span>
        <span class="field-suffix">AM / PM</span>
      </div>
      <div class="day-row">
        <span class="day"><span class="day-box"></span>MON</span>
        <span class="day"><span class="day-box"></span>TUE</span>
        <span class="day"><span class="day-box"></span>WED</span>
        <span class="day"><span class="day-box"></span>THU</span>
        <span class="day"><span class="day-box"></span>FRI</span>
        <span class="day"><span class="day-box"></span>SAT</span>
      </div>
    </div>

    <p class="notice">If unable to keep appointment, kindly give 24hrs notice.</p>
  </section>

  <section class="card contact-card">
    <div class="brand">
      <span class="brand-dot"></span>
      <h1 class="brand-name">Lumen Orto</h1>
    </div>
    <p class="person-name">Daniel Harper</p>
    <p class="person-role">Managing Director</p>
    <p class="address">48 Willow Lane, Eastbrook<br>United Kingdom, EB4 2LT.</p>
    <ul class="contact-list">
      <li>
        <svg class="contact-icon" viewBox="0 0 24 24" aria-hidden="true"><path d="M6.6 10.8a15.1 15.1 0 0 0 6.6 6.6l2.2-2.2a1 1 0 0 1 1-.25 11.4 11.4 0 0 0 3.6.57 1 1 0 0 1 1 1V20a1 1 0 0 1-1 1A17 17 0 0 1 3 4a1 1 0 0 1 1-1h3.5a1 1 0 0 1 1 1c0 1.25.2 2.45.57 3.57a1 1 0 0 1-.25 1z"/></svg>
        044-987 654 321
      </li>
      <li>
        <svg class="contact-icon" viewBox="0 0 24 24" aria-hidden="true"><path d="M2 5h20v14H2z M2 5l10 8 10-8" /></svg>
        hello@lumenorto.com
      </li>
      <li>
        <svg class="contact-icon" viewBox="0 0 24 24" aria-hidden="true"><path d="M10.6 13.4a1 1 0 0 1 0-1.4l4-4a1 1 0 1 1 1.4 1.4l-4 4a1 1 0 0 1-1.4 0zM8 20a5 5 0 0 1-3.5-8.5l2-2 1.4 1.4-2 2a3 3 0 1 0 4.2 4.2l2-2 1.4 1.4-2 2A5 5 0 0 1 8 20zm9.5-5.5-1.4-1.4 2-2a3 3 0 1 0-4.2-4.2l-2 2-1.4-1.4 2-2a5 5 0 1 1 7 7z"/></svg>
        www.lumenorto.com
      </li>
    </ul>
    <p class="tagline">Relax, Renew, Revive</p>
  </section>

</body>
</html>
```